2024 Harwick Patrol Deputy's Statute Handbook

Cover, spine and back cover for our annual law manual. The overall size of the cover is 18.82 x 11 (with the .25 inch bleed it is 19.32 x 11.5) and the spine is 1.82 x 11 plus (1.82 x 11.5 with the bleed).
The book comes with a motor vehicle companion guide which will be 5" X 7" with spiral binding. The companion guide will have the same design with a slight twist related to motor vehicle law.

```html
<!DOCTYPE html>
<html lang="en">
<head>
<meta charset="utf-8">
<title>2024 Harwick Patrol Deputy's Statute Handbook – Cover Spread</title>
<link href="https://fonts.googleapis.com/css2?family=Anton&family=Lexend:wght@400;500&display=swap" rel="stylesheet">
<style>
  :root {
    --page-bg: #ffffff;
    --navy-outer: #0c1148;
    --navy-panel: #070b3b;
    --front-blue: #1c2385;
    --front-deep: #0b1050;
    --gold: #f7be00;
    --white: #ffffff;
    --slate: #224c66;
  }
  * { margin: 0; padding: 0; box-sizing: border-box; }
  html, body { width: 1200px; height: 1112px; overflow: hidden; background: var(--page-bg); }
  .canvas { position: relative; width: 1200px; height: 1112px; }

  .cover-spread {
    position: absolute; left: 28px; top: 245px; width: 1142px; height: 621px;
    background: var(--navy-outer);
  }
  .back-cover {
    position: absolute; left: 14px; top: 14px; width: 481px; height: 594px;
    background: var(--navy-panel);
    font-family: 'Lexend', sans-serif; color: var(--white);
  }
  .back-copy {
    position: absolute; left: 33px; top: 47px; width: 429px;
    font-size: 15.5px; line-height: 26.2px; text-align: justify; hyphens: manual;
  }
  .photo-slot {
    float: left; width: 210px; height: 210px; margin: 5px 24px 10px 0;
    border: 3px solid var(--gold); background: var(--slate);
    display: flex; align-items: center; justify-content: center;
    font-family: 'Anton', sans-serif; font-size: 44px; letter-spacing: 2px; color: var(--white);
  }
  .back-note {
    position: absolute; left: 39px; top: 486px; width: 202px;
    font-size: 15px; line-height: 17.5px; text-align: justify;
  }

  .spine {
    position: absolute; left: 495px; top: 14px; width: 54px; height: 594px;
    background: var(--navy-outer);
  }
  .spine-title {
    position: absolute; left: 27px; top: 22px;
    transform-origin: 0 0; transform: rotate(90deg) translateY(-50%);
    white-space: nowrap; font-family: 'Anton', sans-serif; font-size: 20px; letter-spacing: 0.6px;
    color: var(--white);
  }
  .spine-title .year { color: var(--gold); margin-right: 8px; }

  .front-cover {
    position: absolute; left: 549px; top: 14px; width: 482px; height: 594px;
    background: radial-gradient(ellipse at 45% 30%, var(--front-blue) 0%, #141a6e 45%, var(--front-deep) 100%);
    overflow: hidden;
  }
  .front-art { position: absolute; inset: 0; }
  .front-title {
    position: absolute; left: 49px; top: 22px; width: 385px; text-align: center;
    font-family: 'Anton', sans-serif; color: var(--white);
  }
  .front-year { font-size: 66px; line-height: 84px; color: var(--gold); letter-spacing: 1px; }
  .gold-rule { height: 3px; background: var(--gold); }
  .title-lines { font-size: 47px; line-height: 66px; letter-spacing: 1px; padding: 6px 0 6px; }
  .publisher {
    position: absolute; left: 170px; top: 446px; width: 140px;
    display: flex; flex-direction: column; align-items: center; gap: 8px;
    font-family: 'Lexend', sans-serif; font-weight: 500; font-size: 13px; line-height: 16px;
    color: var(--gold); text-align: center; letter-spacing: 0.5px;
  }
  .publisher-dot { width: 34px; height: 34px; border-radius: 50%; background: var(--gold); }

  .flap {
    position: absolute; left: 1044px; top: 0; width: 98px; height: 621px;
    background: var(--navy-outer);
    font-family: 'Lexend', sans-serif; color: var(--white);
  }
  .flap-year {
    position: absolute; left: 0; top: 33px; width: 98px; text-align: center;
    font-family: 'Anton', sans-serif; font-size: 38px; line-height: 35px; color: var(--gold);
  }
  .flap-copy {
    position: absolute; left: 17px; top: 117px; width: 69px;
    font-size: 14.5px; line-height: 17.5px; text-align: justify; text-align-last: justify;
    letter-spacing: 1px; overflow-wrap: break-word;
  }
</style>
</head>
<body>
<div class="canvas">
  <div class="cover-spread">

    <section class="back-cover">
      <div class="back-copy">
        <div class="photo-slot">PHOTO</div>
        Lorem ipsum dolor sit amet, consectetuer adi­pisczzztetuer adipiscing Lorem ipsum dolor sit amet, consectetuer adi­piscing Lorem ipsum dolor sit amet, consecte­tuer adipiscing Lorem ipsum dolor sit amet, consectetuer adipiscing Lorem ipsum dolaor sit amet, consectetuer adipiscing Lorem ipsum dolor sit amet, consectetuer adipiscing bLorem ipsum dolor sit amet, consectetuer adipiscing Lorem ipsum dolor sit amet, consectetuer adipiscing Lorem ipsum dolor sit amet, consectetuer adipiscing Lorem ipsum dolor sit amet,
      </div>
      <p class="back-note">Lorem ipsum dolor sit amet, consectetuer adi­piscing elit, sed diam no­nummy nibh euismod tin­cidunt ut laoreet dolore</p>
    </section>

    <section class="spine">
      <div class="spine-title"><span class="year">2024</span>HARWICK PATROL DEPUTY'S STATUTE HANDBOOK</div>
    </section>

    <section class="front-cover">
      <div class="front-art" role="img" aria-label="Dark blue photograph of handcuffs on a textured surface with a faint outline map of the region"></div>
      <div class="front-title">
        <div class="front-year">2024</div>
        <div class="gold-rule"></div>
        <h1 class="title-lines">HARWICK PATROL<br>DEPUTY'S STATUTE<br>HANDBOOK</h1>
        <div class="gold-rule"></div>
      </div>
      <div class="publisher">
        <span class="publisher-dot"></span>
        <span>CORRIGAN ACADEMY CONSULTING</span>
      </div>
    </section>

    <aside class="flap">
      <div class="flap-year">20<br>24</div>
      <p class="flap-copy">Lorem ipsum dolor sit amet, consec­tetuer adipis­cing elit, sed diam no­nummy nibh euismod tinci­dunt ut laoreet dolore magna aliquam erat vo­lutpat. Ut wisi enim ad minim veniam,</p>
    </aside>

  </div>
</div>
</body>
</html>
```